Friseur sucht Heftcover für Tipps zur natürlichen Haarpflege
Zielgruppe
Wir sind ein Friseur auf natürlicher Basis und arbeiten ausschließlich mit Naturprodukten.
Hier in diesem Heft sind alle unsere Haartipps zur natürlichen Haarpflege zusammengefasst. Das Heftchen bekommt jeder Kunde aus dem Studio zur Pflege für zuhause.
Zielgruppe sind Frauen im Alter zwischen 30 und 55.
Aufgabenstellung
Unser grundsätzliches Design ist eher schlank und neutral. Das Haarkonzept-Heft soll als Produkt in unser Sortiment einfließen und sieht als Foto eher unattraktiv aus. Außerdem soll es eventuell auch als E-Book erscheinen.
Eigentlich soll es ein typisches aber ansehnliches Produktbild eines typischen E-Books/Buchcovers werden.
Wir brauchen hier eine einfache aber attraktive Darstellung dieser weißen Broschüre. Hintergrund soll ebenfalls oder falls möglich weiß bleiben.

```html
<!DOCTYPE html>
<html lang="de">
<head>
<meta charset="utf-8">
<title>Terra Viva Haarkonzept</title>
<link href="https://fonts.googleapis.com/css2?family=Ubuntu:wght@400;500;700&family=Ubuntu+Condensed&display=swap" rel="stylesheet">
<style>
  :root {
    --bg: #ffffff;
    --paper: #ececec;
    --paper-light: #f3f3f3;
    --ink: #3d3d3d;
    --ink-soft: #6b6b6b;
    --rule: #c9c9c9;
    --numeral: #e0e0e0;
    --green: #8fbf8a;
    --green-soft: #d8ead4;
    --photo-a: #b48a6e;
    --photo-b: #d9d2c8;
  }
  * { box-sizing: border-box; margin: 0; padding: 0; }
  html, body { width: 1200px; height: 684px; overflow: hidden; background: var(--bg); }
  body { font-family: "Ubuntu", sans-serif; color: var(--ink); position: relative; }

  /* Cover */
  .cover {
    position: absolute; left: 40px; top: 94px; width: 350px; height: 496px;
    background: linear-gradient(180deg, var(--paper-light), var(--paper));
    box-shadow: 0 2px 8px rgba(0,0,0,.12);
  }
  .cover__rule { position: absolute; left: 28px; right: 28px; height: 1px; background: var(--rule); }
  .cover__rule--top { top: 70px; }
  .cover__rule--mid { top: 164px; }
  .cover__rule--bottom { bottom: 48px; }
  .cover__title {
    position: absolute; top: 98px; left: 0; right: 0; text-align: center;
    font-weight: 700; font-size: 21px; color: var(--ink-soft); letter-spacing: .2px;
  }
  .cover__emblem { position: absolute; top: 132px; left: 159px; width: 32px; height: 32px; }
  .cover__brand {
    position: absolute; bottom: 72px; left: 0; right: 0; text-align: center;
    font-size: 18px; font-weight: 500; color: var(--ink-soft); letter-spacing: .5px;
  }

  /* Spread */
  .spread {
    position: absolute; left: 420px; top: 94px; width: 740px; height: 496px;
    display: flex; box-shadow: 0 2px 8px rgba(0,0,0,.12);
  }
  .page { width: 370px; height: 100%; background: var(--paper-light); position: relative; }
  .page--left { background: linear-gradient(90deg, var(--paper-light) 85%, #e2e2e2); }
  .page--right { background: linear-gradient(90deg, #e4e4e4, var(--paper-light) 12%); padding: 30px 24px 22px 26px; }

  .step { position: absolute; width: 190px; height: 60px; border: 1px solid var(--rule); text-align: center; }
  .step--right { left: 150px; }
  .step--left { left: 30px; }
  .step__icon {
    position: absolute; top: -22px; left: 77px; width: 36px; height: 36px; border-radius: 50%;
    background: var(--paper-light); border: 1px solid var(--rule);
    display: flex; align-items: center; justify-content: center;
  }
  .step__title { margin-top: 18px; font-size: 9px; font-weight: 500; color: var(--ink); }
  .step__text { font-family: "Ubuntu Condensed", sans-serif; font-size: 6px; line-height: 1.3; color: var(--ink-soft); padding: 3px 8px 0; }
  .numeral { position: absolute; font-size: 90px; font-weight: 700; color: var(--numeral); line-height: 1; }

  .article__title { font-size: 16px; font-weight: 400; color: var(--ink); margin-bottom: 10px; }
  .article__body {
    column-count: 2; column-gap: 12px; height: 232px;
    font-family: "Ubuntu Condensed", sans-serif; font-size: 6.4px; line-height: 1.42;
    text-align: justify; color: var(--ink-soft);
  }
  .article__body p { margin-bottom: 7px; }
  .article__sub { font-family: "Ubuntu", sans-serif; font-size: 9px; font-weight: 500; color: var(--ink); margin: 4px 0 6px; }
  .article__photo {
    margin-top: 8px; height: 196px;
    background: linear-gradient(120deg, var(--photo-b) 0%, var(--photo-a) 55%, var(--photo-b) 100%);
  }
</style>
</head>
<body>

<section class="cover">
  <div class="cover__rule cover__rule--top"></div>
  <h1 class="cover__title">Terra Viva Haarkonzept</h1>
  <svg class="cover__emblem" viewBox="0 0 32 32" aria-hidden="true">
    <circle cx="16" cy="16" r="15" fill="none" stroke="var(--green-soft)" stroke-width="2"/>
    <circle cx="16" cy="16" r="11" fill="var(--green)"/>
    <path d="M16 21 L11 16 A2.8 2.8 0 0 1 16 12.6 A2.8 2.8 0 0 1 21 16 Z" fill="#fff"/>
  </svg>
  <div class="cover__rule cover__rule--mid"></div>
  <div class="cover__brand">Terra Viva</div>
  <div class="cover__rule cover__rule--bottom"></div>
</section>

<section class="spread">
  <div class="page page--left">
    <span class="numeral" style="left:40px;top:40px">1.</span>
    <div class="step step--right" style="top:52px">
      <div class="step__icon"><svg width="16" height="16" viewBox="0 0 16 16"><ellipse cx="8" cy="5" rx="3" ry="4" fill="var(--green)"/><rect x="7.2" y="8" width="1.6" height="7" fill="var(--green)"/></svg></div>
      <div class="step__title">Bürsten</div>
      <div class="step__text">Das richtige Bürsten der Haare ist der erste Schritt zu einer gesunden Kopfhaut und gepflegten Haarlängen.</div>
    </div>

    <span class="numeral" style="left:270px;top:168px">2.</span>
    <div class="step step--left" style="top:182px">
      <div class="step__icon"><svg width="16" height="16" viewBox="0 0 16 16" fill="none" stroke="var(--green)" stroke-width="1.6"><path d="M4 15 V5 A3 3 0 0 1 10 5"/><path d="M8 7 L12 5 L12 9 Z" fill="var(--green)"/></svg></div>
      <div class="step__title">Naturshampoo-Haarwäsche</div>
      <div class="step__text">Haarwäschen mit milden und natürlichen Shampoos schont das Haar und verbessert das Kopfhautklima.</div>
    </div>

    <span class="numeral" style="left:40px;top:296px">3.</span>
    <div class="step step--right" style="top:316px">
      <div class="step__icon"><svg width="16" height="16" viewBox="0 0 16 16" fill="none" stroke="var(--green)" stroke-width="1.4"><circle cx="4" cy="4" r="2.2"/><circle cx="4" cy="12" r="2.2"/><path d="M6 5.5 L15 12 M6 10.5 L15 4"/></svg></div>
      <div class="step__title">Haarschnitte</div>
      <div class="step__text">Unsere Haarschnitte werden nach den natürlichen Vorgaben der eigenen Haarstruktur angelegt. Diese Vorgehensweise bringt Festigkeit, Fülle und Haltbarkeit.</div>
    </div>

    <span class="numeral" style="left:270px;top:400px">4.</span>
    <div class="step step--left" style="top:428px">
      <div class="step__icon"><svg width="16" height="16" viewBox="0 0 16 16"><path d="M3 13 C3 6 7 3 14 2 C13 9 10 13 3 13 Z" fill="var(--green)"/><path d="M3 13 L10 6" stroke="#fff" stroke-width="1"/></svg></div>
      <div class="step__title">Haarpflege</div>
      <div class="step__text">Wir verwenden natürliche Pflegeprodukte mit hochwertigen Inhaltsstoffen, um das Haar langfristig zu unterstützen.</div>
    </div>
  </div>

  <div class="page page--right">
    <h2 class="article__title">Das Bürsten</h2>
    <div class="article__body">
      <p>Mittlerweile geht die Allgemeinheit davon aus, dass das Bürsten lediglich zum Entwirren und Legen der Haare dient. Diese Routine gehörte allerdings auch lange Zeit zur alltäglichen Haarpflege dazu. Letztendlich wurde durch immer mehr Pflegeprodukte versucht, das Bürsten zu ersetzen. Ergebnis dieses Trends sind tägliche Haarwäschen, die die Kopfhaut austrocknen und die körpereigenen Prozesse beeinträchtigen, anstatt sie zu unterstützen. Schnell fettendes Haar wird so zwangsläufig herbeigeführt, wie auch obligatorische Probleme, die mit einer trockenen und vernachlässigten Kopfhaut einhergehen. Daraus resultieren die täglichen Waschzyklen, die dem Nachfetten, Schuppen und Jucken entgegenwirken sollen. Das Bürsten mit einer Wildschweinborstenbürste kann in genau diesen Punkten Abhilfe schaffen und das Haar auf natürliche Weise pflegen.</p>
      <h3 class="article__sub">Die Wildschweinborstenbürste</h3>
      <p>Eine Haarpflegebürste mit festen und natürlichen Wildschweinborsten bildet die Grundlage um diesen alltäglichen Haar- und Kopfhautproblemen entgegenzuwirken. Gerade für die Haarlängen und -spitzen wirkt das Bürsten wie eine Pflegekur. Die natürlich vorhandenen Fette und Nährstoffe werden von der Kopfhaut so über die gesamte Haarstruktur verteilt. Resultat dieser Anwendung sind Glanz und Geschmeidigkeit.</p>
      <p>Gleichzeitig wird durch die feste Borste die Kopfhaut von abfallenden Hautschüppchen, Verschmutzungen und überflüssigen Fetten befreit, ohne dabei auf chemische Mittel zurückzugreifen. Zudem regt die harte Borste die Durchblutung der Kopfhaut an und sorgt so für eine Stimulierung der Haarwurzel. Das alles funktioniert natürlich nur, wenn man auf diese Pflegestoffe zurückgreifen kann. Ein Reduzieren von Haarwäschen ist für ein pflegendes Bürstenergebnis dringend erforderlich. Denn ohne den – in den Haarlängen benötigten – Talg, entsteht kein glanzvolles und kräftiges Ergebnis.</p>
      <p>Wird die dargestellte Bürstenroutine regelmäßig befolgt, so lassen sich die Haarwäschen langfristig auf ein bis zwei Wäschen pro Woche reduzieren.</p>
    </div>
    <div class="article__photo" role="img" aria-label="Foto: Friseurin bürstet einer Kundin mit einer Holzbürste das lange Haar vor einem Spiegel"></div>
  </div>
</section>

</body>
</html>
```